GDFH Business Card

Looking for a business card design to incorporate our branding. We want to only use the colors listing in the Branding Package (attached).
Updates

Target Market(s)

People who need their phone or device fixed.

Industry/Entity Type

Electronics

Contact Information for Business Card

Please use:

Gadget Fix Haven LLC
4870 S Ridgecrest Pkwy
Suite 318
San Antonio, TX 78291

Wendell Thorsby, Store Manager

(210) 555-0147

Requirements
Must have
• Must include the colors that are contained within the Branding Package PDF file.

```html
<!DOCTYPE html>
<html lang="en">
<head>
<meta charset="utf-8">
<title>GDFH Business Card</title>
<link href="https://fonts.googleapis.com/css2?family=Montserrat:wght@400;500;600&display=swap" rel="stylesheet">
<style>
  :root {
    --bg: #cfe8e0;
    --slate: #8fb0b6;
    --amber: #ffbf3f;
    --lime: #d6df5f;
    --orange: #f05a28;
    --ink: #555a5c;
    --white: #ffffff;
  }
  * { box-sizing: border-box; margin: 0; padding: 0; }
  html, body {
    width: 1200px; height: 960px; overflow: hidden;
    background: var(--bg);
    font-family: "Montserrat", sans-serif;
  }
  .sheet {
    width: 1200px; height: 960px;
    display: flex; flex-direction: column; align-items: center; justify-content: center;
    gap: 30px;
  }
  .card {
    position: relative;
    width: 760px; height: 434px;
    border-radius: 28px;
    overflow: hidden;
    box-shadow: 0 8px 24px rgba(40, 90, 80, 0.18);
  }
  .card-art { position: absolute; inset: 0; width: 100%; height: 100%; }

  /* front */
  .card-front { background: var(--slate); }
  .brand {
    position: absolute; left: 70px; top: 190px;
    display: flex; align-items: center; gap: 16px;
  }
  .brand-mark {
    width: 46px; height: 46px; border-radius: 8px;
    background: var(--orange);
  }
  .brand-name {
    font-weight: 500; font-size: 34px; color: var(--orange);
    letter-spacing: 0.5px;
  }

  /* back */
  .card-back { background: var(--amber); }
  .holder {
    position: absolute; left: 350px; top: 90px;
  }
  .holder-name {
    font-weight: 600; font-size: 26px; color: var(--orange);
    text-transform: uppercase; letter-spacing: 1px;
  }
  .holder-title {
    font-weight: 500; font-size: 17px; color: var(--ink); margin-top: 2px;
  }
  .contact-band {
    position: absolute; left: 340px; right: 0; top: 168px; height: 170px;
    background: var(--lime);
    padding: 16px 24px;
    display: flex; flex-direction: column; justify-content: center; gap: 12px;
  }
  .contact-row {
    display: flex; align-items: center; gap: 14px;
    font-size: 17px; color: var(--ink); line-height: 1.25;
  }
  .contact-icon {
    flex: none; width: 34px; height: 34px; border-radius: 50%;
    background: var(--orange);
    display: flex; align-items: center; justify-content: center;
  }
  .contact-icon svg { width: 18px; height: 18px; }
</style>
</head>
<body>
<main class="sheet">

  <section class="card card-front" aria-label="Card front">
    <svg class="card-art" viewBox="0 0 760 434" preserveAspectRatio="none" aria-hidden="true">
      <polygon fill="var(--amber)" points="340,0 480,0 650,170 520,434 390,434 530,170 380,20"/>
      <polygon fill="var(--amber)" points="520,0 660,0 760,70 760,250 670,434 560,434 690,170"/>
    </svg>
    <div class="brand">
      <span class="brand-mark"></span>
      <span class="brand-name">Gadget Fix Haven</span>
    </div>
  </section>

  <section class="card card-back" aria-label="Card back">
    <svg class="card-art" viewBox="0 0 760 434" preserveAspectRatio="none" aria-hidden="true">
      <polygon fill="var(--slate)" points="170,0 290,0 70,300 0,300 0,230"/>
      <polygon fill="var(--slate)" points="0,300 70,300 470,434 300,434 0,370"/>
    </svg>
    <div class="holder">
      <p class="holder-name">Wendell Thorsby</p>
      <p class="holder-title">Store Manager</p>
    </div>
    <div class="contact-band">
      <div class="contact-row">
        <span class="contact-icon">
          <svg viewBox="0 0 24 24"><path fill="var(--white)" d="M12 2a7 7 0 0 0-7 7c0 5 7 13 7 13s7-8 7-13a7 7 0 0 0-7-7zm0 9.5A2.5 2.5 0 1 1 12 6.5a2.5 2.5 0 0 1 0 5z"/></svg>
        </span>
        <span>4870 S Ridgecrest Pkwy<br>Suite 318, San Antonio, TX 78291</span>
      </div>
      <div class="contact-row">
        <span class="contact-icon">
          <svg viewBox="0 0 24 24"><path fill="var(--white)" d="M6.6 10.8a15 15 0 0 0 6.6 6.6l2.2-2.2a1 1 0 0 1 1-.25 11.4 11.4 0 0 0 3.6.6 1 1 0 0 1 1 1V20a1 1 0 0 1-1 1A17 17 0 0 1 3 4a1 1 0 0 1 1-1h3.5a1 1 0 0 1 1 1c0 1.25.2 2.45.6 3.6a1 1 0 0 1-.25 1z"/></svg>
        </span>
        <span>(210) 555-0147</span>
      </div>
      <div class="contact-row">
        <span class="contact-icon">
          <svg viewBox="0 0 24 24"><path fill="var(--white)" d="M3 5h18a1 1 0 0 1 1 1v12a1 1 0 0 1-1 1H3a1 1 0 0 1-1-1V6a1 1 0 0 1 1-1zm9 7.5L4 7.5V17h16V7.5z"/></svg>
        </span>
        <span>wthorsby@gadgetfixhaven.example</span>
      </div>
    </div>
  </section>

</main>
</body>
</html>
```